Therapeutic Counselling Practice Brochure

I have a new therapeutic counselling practice in Melbourne.

I am making peri natal issues my special interest area.

I need a brochure targeted at new parents or pregnant women and partners, struggling with the concept of parenting, depression, maybe do not even know about it.

The feel should be safe and strong. I love the KESTA website ( I do volunteer work with them)

Out of hours appointments and telephone counselling are important making my service very accessible.

Attached is an example for the content of the Brochure

Attached is an example for the content of the Brochure.

Target Market(s)

25 - 45 New Parents , expectant parents,families and friends of people struggling emotionally and mentally with and around being new parents

Requirements
Must have
• Feel of safety, somewhere to go for help, support, a conversation, soft ,strong
Nice to have
• mother and child, maybe parents and child, possibly a graphic, faceless

```html
<!DOCTYPE html>
<html lang="en">
<head>
<meta charset="utf-8">
<title>Maren Holloway – Counsellor and Personal Coach brochure</title>
<link href="https://fonts.googleapis.com/css2?family=Open+Sans:ital,wght@0,400;0,600;0,700;0,800;1,400;1,700&display=swap" rel="stylesheet">
<style>
  :root {
    --green-dark: #3f7c1e;
    --green: #6aab2a;
    --green-lime: #9fcc45;
    --green-pale: #d9ecb4;
    --teal: #2f6f8c;
    --ink: #333a33;
    --paper: #ffffff;
    --bg: #eceee8;
    --sky: #cfe4f2;
  }
  * { box-sizing: border-box; margin: 0; padding: 0; }
  html, body { width: 1200px; height: 846px; overflow: hidden; }
  body {
    background: var(--bg);
    font-family: "Open Sans", Arial, sans-serif;
    color: var(--ink);
    position: relative;
  }
  .sheet { position: absolute; top: 160px; height: 520px; display: flex; box-shadow: 0 6px 22px rgba(0,0,0,.18); }
  .sheet--inside { left: 25px; }
  .sheet--outside { left: 727px; }
  .panel {
    position: relative; width: 224px; height: 520px;
    background: var(--paper); overflow: hidden;
    border-right: 1px solid #e3e6df;
  }
  .panel:last-child { border-right: none; }
  .band { position: absolute; left: 0; width: 100%; display: block; }
  .band--top { top: 0; height: 46px; }
  .band--bottom { bottom: 0; height: 40px; }
  .photo { position: absolute; display: block; }
  .copy { position: absolute; left: 16px; right: 14px; font-size: 7.4px; line-height: 1.45; }
  .copy p { margin-bottom: 7px; }

  /* inside left */
  .photo--mother-baby-soft { top: 30px; left: 88px; width: 136px; height: 100px;
    background: radial-gradient(ellipse at 60% 45%, #c9d3d8 0%, #e9eef0 55%, rgba(255,255,255,0) 80%); }
  .depression-title { position: absolute; top: 60px; left: 16px; color: var(--teal);
    font-size: 13px; font-weight: 700; line-height: 1.2; }
  .copy--intro { top: 135px; text-align: justify; }
  .symptoms { list-style: none; margin-left: 16px; }
  .symptoms li::before { content: "• "; }

  /* inside middle */
  .photo--sky { top: 22px; left: 0; width: 224px; height: 120px;
    background: linear-gradient(180deg, #a9cde6 0%, var(--sky) 55%, #ffffff 100%); }
  .copy--middle { top: 60px; text-align: justify; font-size: 7.6px; }
  .photo--consultation { top: 270px; left: 0; width: 224px; height: 212px;
    background: linear-gradient(160deg, #f1f3f4 0%, #dfe5e8 45%, #c7ced2 100%); }

  /* inside right */
  .care-title { position: absolute; top: 22px; left: 16px; color: var(--green-dark);
    font-size: 12.5px; font-weight: 400; }
  .copy--care { top: 52px; }
  .copy--care h3 { font-size: 7.4px; font-weight: 700; }
  .copy--care p { margin-bottom: 5px; }

  /* back panel */
  .photo--portrait { top: 0; left: 0; width: 224px; height: 148px;
    background: linear-gradient(90deg, #f4f1ec 0%, #e8d7c6 45%, #cfe0b0 100%); }
  .name-bar { position: absolute; top: 152px; left: 14px; width: 210px; height: 18px;
    background: linear-gradient(90deg, var(--green-pale), #ffffff);
    font-size: 8px; font-weight: 700; padding: 3px 10px; }
  .copy--contact { top: 184px; font-size: 7.6px; }
  .copy--contact strong { font-weight: 700; }
  .booking { position: absolute; top: 420px; left: 0; width: 100%; text-align: center;
    font-size: 7.6px; line-height: 1.5; }

  /* cover */
  .cover-head { position: absolute; top: 0; left: 0; width: 224px; height: 70px;
    background: var(--green-dark); color: #fff; }
  .brand { position: absolute; top: 14px; left: 14px; display: flex; align-items: flex-start; gap: 8px; }
  .brand__mark { width: 22px; height: 22px; border-radius: 50%; background: var(--green-lime); flex: none; }
  .brand__name { font-size: 13px; font-weight: 700; line-height: 1.1; }
  .brand__role { font-size: 7.5px; font-weight: 700; margin-top: 2px; }
  .photo--mother-baby { top: 62px; left: 0; width: 224px; height: 205px;
    background: linear-gradient(135deg, #d9a98e 0%, #f0d6c4 45%, #f7ebe2 100%); }
  .cover-curve { position: absolute; top: 50px; left: 0; width: 224px; height: 40px; display: block; }
  .headline { position: absolute; top: 276px; left: 12px; right: 10px; color: var(--green-dark);
    font-size: 13.4px; font-weight: 800; line-height: 1.2; letter-spacing: .2px; }
  .subhead { position: absolute; top: 312px; left: 12px; color: var(--green);
    font-size: 11px; font-style: italic; font-weight: 700; }
  .cover-copy { position: absolute; top: 334px; left: 12px; right: 10px; color: var(--green-dark);
    font-size: 7.8px; font-style: italic; line-height: 1.35; }
  .cover-swoosh { position: absolute; bottom: 0; left: 0; width: 224px; height: 120px; display: block; }
</style>
</head>
<body>

<section class="sheet sheet--inside" aria-label="Brochure inside">
  <article class="panel panel--depression">
    <svg class="band band--top" viewBox="0 0 224 46" preserveAspectRatio="none"><path d="M0 0H224V14Q110 44 0 30Z" fill="var(--green)"/><path d="M0 30Q110 44 224 14V20Q110 50 0 36Z" fill="var(--green-pale)"/></svg>
    <div class="photo photo--mother-baby-soft" role="img" aria-label="Soft photo of a mother holding her baby"></div>
    <h2 class="depression-title">DEPRESSION-<br>During and<br>After<br>Pregnancy</h2>
    <div class="copy copy--intro">
      <p>Depression is more than just the “Baby Blues” (feeling weepy and irritable), or feeling “down in the dumps” for a few days. With depression, sad, anxious or empty feelings don’t go away.</p>
      <p>They interfere with your daily life and routines. The good news is that most people with depression get better with treatment.</p>
      <p>How do I know if I have depression?<br>If you have any of the following symptoms for more than two weeks:</p>
      <ul class="symptoms">
        <li>Feeling restless or moody</li>
        <li>Feeling sad, hopeless and overwhelmed</li>
        <li>Crying</li>
        <li>Having no energy or motivation</li>
        <li>Eating too much or too little</li>
        <li>Sleeping too much or too little</li>
        <li>Withdrawing from family or friends</li>
        <li>Having memory problems</li>
        <li>Feeling worthless or guilty</li>
        <li>Experiencing headaches, aches and pains</li>
        <li>Having trouble focusing or making decisions</li>
        <li>Losing interest in pleasurable activities you used to enjoy.</li>
      </ul>
    </div>
    <svg class="band band--bottom" viewBox="0 0 224 40" preserveAspectRatio="none"><path d="M0 40V24Q120 4 224 18V40Z" fill="var(--green-lime)"/></svg>
  </article>

  <article class="panel panel--support">
    <div class="photo photo--sky" role="img" aria-label="Photo of a soft blue sky with light clouds"></div>
    <svg class="band band--top" viewBox="0 0 224 46" preserveAspectRatio="none"><path d="M0 0H224V8Q110 26 0 14Z" fill="var(--green)"/></svg>
    <div class="copy copy--middle">
      <p>Depression impacts on the whole family, including baby. You may feel guilty and a “not good enough mother”, you may lose confidence.</p>
      <p>Depression can be treated with counselling, “talk therapy”. A check up at your doctor is advisable too.</p>
      <p>Postpartum depression doesn’t discriminate. It affects women of all ages, cultural and social standing.</p>
      <p>“Sometimes”, said Bramble “The smallest thing takes up the most room in your heart.”</p>
    </div>
    <div class="photo photo--consultation" role="img" aria-label="Photo of a doctor listening to a worried young woman"></div>
    <svg class="band band--bottom" viewBox="0 0 224 40" preserveAspectRatio="none"><path d="M0 40V20Q110 2 224 24V40Z" fill="var(--green-lime)"/><path d="M0 40V30Q110 14 224 34V40Z" fill="var(--green)"/></svg>
  </article>

  <article class="panel panel--care">
    <svg class="band band--top" viewBox="0 0 224 46" preserveAspectRatio="none"><path d="M0 0H224V6Q110 20 0 10Z" fill="var(--green)"/></svg>
    <h2 class="care-title">Looking after yourself</h2>
    <div class="copy copy--care">
      <h3>Rest</h3>
      <p>Sleep if you can, and have a rest if you can’t. Nap when your baby is sleeping.</p>
      <h3>Diet</h3>
      <p>Eat a healthy, well balanced diet. With all the new demands on your body, good nutrition is very important. Try not to skip meals.</p>
      <h3>Exercise</h3>
      <p>Although it may be the last thing you feel like doing, some gentle exercise will help you to feel better both physically and mentally. Just going for a walk with baby can help.</p>
      <h3>Meditate</h3>
      <p>It may be difficult to quieten your mind; a guided meditation on CD may help.</p>
      <h3>Stay connected</h3>
      <p>Having a baby can make you feel isolated. Talk with other new mothers, join a support group.</p>
      <h3>Be kind to yourself</h3>
      <p>You need to take care of yourself to take care of your baby. Don’t load yourself with extra tasks. Housework doesn’t need to be done perfectly. Know how little can be enough.</p>
      <h3>Help</h3>
      <p>Ask and accept help from family and friends, with meals, shopping or minding baby. You may be surprised how much the people who surround you want to share the load and share here.</p>
    </div>
    <svg class="band band--bottom" viewBox="0 0 224 40" preserveAspectRatio="none"><path d="M0 40V26Q110 6 224 16V40Z" fill="var(--green)"/></svg>
  </article>
</section>

<section class="sheet sheet--outside" aria-label="Brochure outside">
  <article class="panel panel--contact">
    <div class="photo photo--portrait" role="img" aria-label="Portrait photo of the counsellor smiling"></div>
    <div class="name-bar">Maren Holloway J.P.</div>
    <div class="copy copy--contact">
      <p><strong>Office:</strong><br>Level 2, 48 Linden Street, Southbank 3006</p>
      <p><em>Evening and weekend appointments available.</em></p>
      <p><strong>Telephone Counselling</strong> saves travel time and the hassle of parking.</p>
      <p>Telephone counselling gives you a flexible option in accessing therapy.</p>
      <p>Some people feel more comfortable discussing issues over the telephone, safe supportive and confidential.</p>
      <p><strong><em>Telephone appointments are available within 48 hours.</em></strong></p>
    </div>
    <div class="booking">To book please contact<br>Maren Holloway<br>on 0400 123 456<br>maren@marenholloway.com.au<br>www.marenholloway.com.au</div>
    <svg class="band band--bottom" viewBox="0 0 224 40" preserveAspectRatio="none"><path d="M0 40V22Q110 10 224 20V40Z" fill="var(--green-pale)"/><path d="M0 40V30Q110 20 224 28V40Z" fill="var(--green-lime)"/></svg>
  </article>

  <article class="panel panel--cover">
    <div class="photo photo--mother-baby" role="img" aria-label="Photo of a smiling mother cuddling her baby"></div>
    <svg class="cover-curve" viewBox="0 0 224 40" preserveAspectRatio="none"><path d="M0 0H224V14Q120 18 0 40Z" fill="var(--green-dark)"/><path d="M0 40Q120 18 224 14V20Q120 24 0 46Z" fill="var(--green-lime)"/></svg>
    <header class="cover-head">
      <div class="brand">
        <span class="brand__mark"></span>
        <div>
          <div class="brand__name">Maren Holloway</div>
          <div class="brand__role">Counsellor and Personal Coach</div>
        </div>
      </div>
    </header>
    <h1 class="headline">ARE YOU EXPECTING<br>OR A NEW PARENT?</h1>
    <p class="subhead">Got the “Baby Blues”?</p>
    <p class="cover-copy">There is an expectation of happiness and fulfilment around childbirth.<br>Feeling “blue”, interferes with the adjustment to becoming a parent.<br>Sharing your feelings by talking is important.</p>
    <svg class="cover-swoosh" viewBox="0 0 224 120" preserveAspectRatio="none"><path d="M0 120V70Q120 70 224 10V120Z" fill="var(--green-lime)"/><path d="M0 120V92Q130 88 224 40V120Z" fill="var(--green)"/><path d="M0 120V108Q140 104 224 74V120Z" fill="var(--green-dark)"/></svg>
  </article>
</section>

</body>
</html>
```